Lumora Wellness - Professional Sales Presentation

Lumora Wellness needs to take it's professional sales presentation to the next level. The finished product must be engaging, elegant and trustworthy. In 20 slides or less, our value proposition needs to be crisply communicated. We will be using this presentation for Webinars and in print form, so this project requires a designer with deep powerpoint presentation experience. Both are very important ... 1) How the presentation is revealed live, and 2) How it appears in print form.

I've attached a draft presentation along with AI and JPG versions of our logo. Please visit LumoraWellness.example for insight on our services. Be certain to watch the video on our home page to learn what we do ... you'll be inspired! The winning presentation will be presented in boardrooms at Meridian 700 companies across America.

I'll interact frequently with those who take this project seriously and bring their very best work to the table ... you'll be working directly with Lumora's CEO.

You're invited to knock my socks off :)

Gregor

Target Market(s)

Meridian 700 Executives - the head of Benefits or Human Resources

Industry/Entity Type

Health Care

Font styles to use
Sans Serif
Script

Colors
ec1f27

Requirements
Must have
• Must be very professional, but creatively engaging, no more than 20 slides. Board rooms are inundated with BORING presentations ... that can't be this one. It needs to stand out, without going over the top.
Nice to have
• I need to be able to edit the text you'll find in my DRAFT presentation so please don't just create and use graphic files. Feel free to create cool graphic elements that are revealed at various points, but the next needs to be editable throughout.
Should not have
• Can't be cheesy, cheap or gimmicky. Must be completely credible.

```html
<!DOCTYPE html>
<html lang="en">
<head>
<meta charset="utf-8">
<title>Lumora Wellness – Sales Presentation Slide</title>
<link rel="stylesheet" href="https://fonts.googleapis.com/css2?family=Roboto+Condensed:wght@300;400;700&display=swap">
<style>
  :root {
    --brand-red: #ec1f27;
    --header-red: #ee3124;
    --ink: #4a4a4a;
    --footer-bg: #333333;
    --paper: #ffffff;
  }
  * { box-sizing: border-box; margin: 0; padding: 0; }
  html, body { width: 1200px; height: 900px; overflow: hidden; background: var(--paper); }
  body { font-family: "Roboto Condensed", "Arial Narrow", sans-serif; }

  .slide { position: relative; width: 1200px; height: 900px; background: var(--paper); }

  .slide-header {
    position: absolute; left: 0; top: 0; width: 1200px; height: 76px;
    background: var(--header-red);
  }
  .slide-title {
    position: absolute; left: 20px; top: 10px;
    color: var(--paper); font-weight: 400; font-size: 44px; line-height: 56px;
    letter-spacing: 0.2px;
  }
  .brand-box {
    position: absolute; left: 964px; top: 0; width: 214px; height: 76px;
    background: var(--paper);
    display: flex; align-items: center; justify-content: center;
  }
  .brand-name {
    color: var(--brand-red); font-weight: 700; font-size: 27px; line-height: 1;
  }

  .question-list { list-style: none; position: absolute; left: 0; top: 0; }
  .question {
    position: absolute; left: 83px; width: 1060px;
    color: var(--ink); font-weight: 300; font-size: 25px; line-height: 34.5px;
  }
  .question svg {
    position: absolute; left: -46px; top: 8px; width: 20px; height: 20px;
  }

  .closing-question {
    position: absolute; left: 48px; top: 726px; width: 1120px;
    color: var(--brand-red); font-weight: 700; font-size: 26px; line-height: 42px;
  }

  .slide-footer {
    position: absolute; left: 0; top: 858px; width: 1200px; height: 42px;
    background: var(--footer-bg);
    color: var(--paper); font-weight: 400; font-size: 21px; line-height: 42px;
  }
  .copyright { position: absolute; left: 9px; }
  .page-number { position: absolute; right: 12px; }
</style>
</head>
<body>
<main class="slide">
  <header class="slide-header">
    <h1 class="slide-title">Project Title Here</h1>
    <div class="brand-box"><span class="brand-name">Lumora Wellness</span></div>
  </header>

  <ul class="question-list">
    <li class="question" style="top:154px">
      <svg viewBox="0 0 20 20" aria-hidden="true"><path d="M4 2 L14 10 L4 18 L8 10 Z" fill="var(--brand-red)"/></svg>
      What percentage of your employees are getting their periodic preventive visits with a PCP?
    </li>
    <li class="question" style="top:226px">
      <svg viewBox="0 0 20 20" aria-hidden="true"><path d="M4 2 L14 10 L4 18 L8 10 Z" fill="var(--brand-red)"/></svg>
      When you conduct biometric screenings, what, beyond participation, is defined as success?
    </li>
    <li class="question" style="top:298px">
      <svg viewBox="0 0 20 20" aria-hidden="true"><path d="M4 2 L14 10 L4 18 L8 10 Z" fill="var(--brand-red)"/></svg>
      Why do companies do biometric screenings in the first place? (Hint: Because people don’t get<br>their periodic preventive visits)
    </li>
    <li class="question" style="top:406px">
      <svg viewBox="0 0 20 20" aria-hidden="true"><path d="M4 2 L14 10 L4 18 L8 10 Z" fill="var(--brand-red)"/></svg>
      What percentage of those identified as needing to see a PCP for “out of range” biometrics<br>actually see one in a timely way?
    </li>
    <li class="question" style="top:514px">
      <svg viewBox="0 0 20 20" aria-hidden="true"><path d="M4 2 L14 10 L4 18 L8 10 Z" fill="var(--brand-red)"/></svg>
      What percentage of high risk employees are engaging with your disease and health/wellness<br>programs?
    </li>
    <li class="question" style="top:622px">
      <svg viewBox="0 0 20 20" aria-hidden="true"><path d="M4 2 L14 10 L4 18 L8 10 Z" fill="var(--brand-red)"/></svg>
      What percentage of the “screening” results are re-run by a PCP, either because they don’t<br>receive them or they doubt their accuracy?
    </li>
  </ul>

  <p class="closing-question">What are the true costs of your current “screen – refer – PCP visit – retest” paradigm?<br>(Hint:&nbsp; About $300, all in)</p>

  <footer class="slide-footer">
    <span class="copyright">Copyright text here</span>
    <span class="page-number">Page : 01</span>
  </footer>
</main>
</body>
</html>
```